Marvanta DRC Box Design - Organic

Pellin Harvest Foods is refreshing the Marvanta DRC (Display-Ready Case) packaging for Organic Uncooked Flour Tortillas. The existing box design (reference: Sunleaf Wrap Rustica Blend DRC) should serve as an inspiration as well as the new website: www.pellinharvestfoods.example.

Requirements
Nice to have
• Use the website as a reference point www.pellinharvestfoods.example

```html
<!DOCTYPE html>
<html lang="en">
<head>
<meta charset="utf-8">
<title>Marvanta DRC Box – Organic Uncooked Flour Tortillas</title>
<link rel="stylesheet" href="https://fonts.googleapis.com/css2?family=Libre+Baskerville:wght@400;700&display=swap">
<style>
  :root {
    --backdrop: #4a2103;
    --board: #f2e8cc;
    --ink: #4a2a0a;
    --lace-dark: #6b3a14;
    --lace-light: #c9a57d;
  }
  html, body {
    margin: 0;
    padding: 0;
    width: 1200px;
    height: 1200px;
    overflow: hidden;
    background: var(--backdrop);
  }
  .dieline {
    position: relative;
    width: 1200px;
    height: 1200px;
    font-family: "Libre Baskerville", Georgia, serif;
    color: var(--ink);
  }
  .dieline svg { position: absolute; left: 0; top: 0; }
  .label {
    position: absolute;
    margin: 0;
    text-align: center;
    font-weight: 700;
    white-space: nowrap;
    transform: translateX(-50%);
    line-height: 1;
  }
  .end-title { font-size: 22px; letter-spacing: -0.3px; }
  .side-title { font-size: 37px; letter-spacing: 4px; }
  .claim { font-size: 12px; letter-spacing: 2px; }
  .handling {
    font-size: 7px;
    letter-spacing: 1px;
    word-spacing: 2px;
  }
  .handling span + span { margin-left: 12px; }
  .brand-name {
    position: absolute;
    margin: 0;
    transform: translate(-50%, -50%);
    font-weight: 700;
    white-space: nowrap;
    color: var(--ink);
    line-height: 1;
  }
  .brand-name.small { font-size: 19px; letter-spacing: 1px; }
  .brand-name.large { font-size: 23px; letter-spacing: 1px; }
</style>
</head>
<body>
<main class="dieline">
  <svg width="1200" height="1200" viewBox="0 0 1200 1200">
    <defs>
      <linearGradient id="lace" x1="0" y1="0" x2="0" y2="1">
        <stop offset="0" stop-color="var(--lace-light)"/>
        <stop offset="0.5" stop-color="var(--lace-dark)"/>
        <stop offset="1" stop-color="var(--lace-light)"/>
      </linearGradient>
    </defs>

    <g class="blank-upper">
      <path class="board" fill="var(--board)"
            d="M117 46 H527 V244 Q527 272 555 272 H950 Q978 272 978 244 V46 H1087 V564 H117 Z"/>
      <g role="img" aria-label="Lace ornament border">
        <rect x="117" y="46" width="410" height="103" fill="url(#lace)" opacity="0.55"/>
        <rect x="978" y="46" width="109" height="103" fill="url(#lace)" opacity="0.55"/>
      </g>
      <g role="img" aria-label="Lace ornament strip">
        <rect x="117" y="381" width="970" height="28" fill="url(#lace)" opacity="0.6"/>
      </g>
      <line class="fold" x1="425.5" y1="46" x2="425.5" y2="381" stroke="var(--ink)" stroke-width="1"/>
      <rect class="slot" x="421" y="422" width="9" height="145" rx="4.5" fill="var(--backdrop)"/>
    </g>

    <g class="blank-lower">
      <rect class="board" x="117" y="620" width="970" height="528" fill="var(--board)"/>
      <g role="img" aria-label="Lace ornament border">
        <rect x="117" y="620" width="970" height="103" fill="url(#lace)" opacity="0.55"/>
      </g>
      <g role="img" aria-label="Lace ornament strip">
        <rect x="117" y="964" width="970" height="28" fill="url(#lace)" opacity="0.6"/>
      </g>
      <line class="fold" x1="425.5" y1="620" x2="425.5" y2="964" stroke="var(--ink)" stroke-width="1"/>
      <rect class="slot" x="421" y="1006" width="9" height="145" rx="4.5" fill="var(--backdrop)"/>
    </g>

    <g class="brand-seal">
      <circle cx="271" cy="180" r="76" fill="var(--board)" stroke="var(--lace-dark)" stroke-width="3"/>
      <circle cx="271" cy="761" r="76" fill="var(--board)" stroke="var(--lace-dark)" stroke-width="3"/>
      <circle cx="756" cy="773" r="89" fill="var(--board)" stroke="var(--lace-dark)" stroke-width="3"/>
    </g>
  </svg>

  <!-- upper end panel -->
  <p class="brand-name small" style="left:271px; top:180px;">Marvanta</p>
  <p class="label end-title" style="left:271px; top:270px;">UNCOOKED</p>
  <p class="label end-title" style="left:271px; top:300px;">FLOUR TORTILAS</p>
  <p class="label claim" style="left:271px; top:341px;">ORGANIC · NON-GMO</p>
  <p class="label handling" style="left:271px; top:367px;"><span>HANDLE WITH CARE</span><span>PERISHABLE</span><span>KEEP REFRIGERATED</span></p>

  <!-- upper side panel -->
  <p class="label side-title" style="left:758px; top:286px;">UNCOOKED</p>
  <p class="label side-title" style="left:758px; top:335px;">FLOUR TORTILAS</p>

  <!-- lower end panel -->
  <p class="brand-name small" style="left:271px; top:761px;">Marvanta</p>
  <p class="label end-title" style="left:271px; top:852px;">UNCOOKED</p>
  <p class="label end-title" style="left:271px; top:882px;">FLOUR TORTILAS</p>
  <p class="label claim" style="left:271px; top:923px;">ORGANIC</p>
  <p class="label handling" style="left:271px; top:949px;"><span>HANDLE WITH CARE</span><span>PERISHABLE</span><span>KEEP REFRIGERATED</span></p>

  <!-- lower side panel -->
  <p class="brand-name large" style="left:756px; top:773px;">Marvanta</p>
  <p class="label side-title" style="left:758px; top:873px;">UNCOOKED</p>
  <p class="label side-title" style="left:758px; top:922px;">FLOUR TORTILAS</p>
</main>
</body>
</html>
```